Quiet Harbor Path - Web design

I require a complete design for a responsive 3 page business website.

High end design type, similar to (in order of preference):
]https://brennaolstead.co/
https://riverstone-guidance-wellbeing.com.au/
https://calmridgementoring.com.au/
https://buildyourglow.com/
https://theclearpathguide.com/
https://www.dervlakempson.com/
https://theloom.com/

Please use the attached old company logo, which is to be used a reference for the new branding and design.

Please use the colour palette below
#3D3D3D
#FBF8F3
#CAAD53
#7EB492
#EDCFBF

Target Market(s)

Male & female 30-50s, small business owners and executive corporates, first world english speaking nations.

Industry/Entity Type

Life Coaching

Logo Text

Quiet Harbor Path. Tagline: Holistic Transformational Coaching

Number of Pages Required

3 page

Font styles to use
Sans Serif

Requirements
Must have
• Testimonials section, google reivews section, book online button.

```html
<!DOCTYPE html>
<html lang="en">
<head>
<meta charset="utf-8">
<title>Quiet Harbor Path — Holistic Transformational Coaching</title>
<link href="https://fonts.googleapis.com/css2?family=Outfit:wght@300;400;500;600;700;800&display=swap" rel="stylesheet">
<style>
:root{
  --ink:#3d3d3d;
  --cream:#f9f5ef;
  --gold:#c9a550;
  --teal:#0f6b68;
  --teal-dark:#0d6360;
  --line:#d9d9d9;
  --muted:#6b6b6b;
  --footer:#3e3e3e;
  --white:#ffffff;
}
*{box-sizing:border-box;margin:0;padding:0}
html,body{width:1200px;height:4304px;overflow:hidden;background:var(--white)}
body{position:relative;font-family:"Outfit",sans-serif;color:var(--ink)}
.abs{position:absolute}
.btn{position:absolute;background:var(--teal);color:var(--white);font-size:14px;font-weight:500;display:flex;align-items:center;justify-content:center;border-radius:3px}

/* header */
.site-header{position:absolute;left:0;top:0;width:1200px;height:105px;background:var(--white)}
.brand{position:absolute;left:112px;top:30px;display:flex;align-items:center;gap:12px;font-size:30px;font-weight:300;color:var(--ink)}
.brand-dot{width:30px;height:30px;border-radius:50%;background:var(--teal)}
.nav{position:absolute;left:475px;top:43px;display:flex;gap:26px;font-size:13px;font-weight:500}
.nav .active{color:var(--teal)}

/* hero */
.hero{position:absolute;left:0;top:105px;width:1200px;height:512px;background:linear-gradient(90deg,#e6e7e6 0%,#d7d9d6 35%,#c9c6bf 60%,#8f8a80 100%)}
.hero-title{position:absolute;left:156px;top:150px;font-size:98px;font-weight:800;letter-spacing:1px;color:#151515;line-height:1}
.hero-sub{position:absolute;left:161px;top:268px;font-size:24px;font-weight:400;color:#1e1e1e}
.arrow{position:absolute;width:36px;height:36px;border-radius:3px;display:flex;align-items:center;justify-content:center}
.arrow svg{width:14px;height:14px}

/* services */
.section-title{position:absolute;left:0;width:1200px;text-align:center;font-size:34px;font-weight:500;color:var(--ink)}
.card{position:absolute;width:208px;height:244px;background:var(--white);box-shadow:0 3px 14px rgba(0,0,0,.09);border-radius:3px;text-align:center}
.card .icon{position:absolute;left:62px;top:28px;width:84px;height:84px;border-radius:50%;border:2px solid #dfe7e6;background:radial-gradient(circle,#f6efd9 0%,#e9f1ee 70%)}
.card .icon.filled{background:var(--teal);border-color:var(--teal)}
.card h3{position:absolute;left:8px;right:8px;top:132px;font-size:13.5px;font-weight:600;line-height:19px}
.card p{position:absolute;left:14px;right:14px;top:178px;font-size:12.5px;line-height:21px;color:var(--muted)}

/* about */
.about{position:absolute;left:0;top:1369px;width:1200px;height:579px;background:var(--cream)}
.about-photo{position:absolute;left:160px;top:50px;width:400px;height:435px;border-radius:50%;background:radial-gradient(circle at 50% 40%,#f4eadf 0%,#cfc3b6 55%,#6b7180 100%)}
.about h2{position:absolute;left:632px;top:100px;font-size:34px;font-weight:600}
.about .kicker{position:absolute;left:632px;top:148px;font-size:18px;color:var(--gold);font-weight:500}
.about .lead{position:absolute;left:632px;top:212px;width:410px;font-size:14px;font-weight:600;line-height:24px}
.about .body{position:absolute;left:632px;top:268px;width:410px;font-size:12.5px;line-height:24.3px;color:#555}

/* testimonials */
.quote-card{position:absolute;background:var(--white);box-shadow:0 3px 16px rgba(0,0,0,.09);border-radius:3px;text-align:center;overflow:hidden}
.quote-card p{font-style:italic;color:#444}
.quote-card .who{font-weight:600;color:var(--teal)}
.dots{position:absolute;top:2360px;left:577px;display:flex;gap:6px}
.dots span{width:7px;height:7px;border-radius:50%;background:#e5e5e5}
.dots span.on{background:var(--gold)}

/* start */
.start-title{position:absolute;left:162px;top:2500px;font-size:58px;font-weight:600;line-height:70px}
.start-text{position:absolute;left:162px;top:2658px;width:460px;font-size:19px;font-weight:500;line-height:37px}
.start-photo{position:absolute;left:638px;top:2435px;width:400px;height:422px;border-radius:6px;background:linear-gradient(160deg,#3b3b3b 0%,#d9d6d1 45%,#9a7b5f 80%,#4d3a2d 100%)}

/* contact */
.contact{position:absolute;left:232px;top:2958px;width:736px;height:506px;background:var(--white);box-shadow:0 4px 20px rgba(0,0,0,.08)}
.contact h2{position:absolute;left:0;right:0;top:66px;text-align:center;font-size:34px;font-weight:500}
.contact .intro{position:absolute;left:0;right:0;top:120px;text-align:center;font-size:14px;color:#555}
.field{position:absolute;border:1px solid var(--line);font-size:11px;color:#777;padding:9px 14px}
.fold{position:absolute;right:0;bottom:0;width:0;height:0;border-left:38px solid var(--teal);border-top:36px solid transparent}
.fold-cut{position:absolute;right:0;bottom:0;width:0;height:0;border-right:38px solid var(--white);border-top:36px solid transparent}

/* instagram */
.insta-title{position:absolute;left:0;width:1200px;top:3556px;text-align:center;font-size:32px;font-weight:700}
.insta-handle{position:absolute;left:0;width:1200px;top:3598px;text-align:center;font-size:14px}
.tile{position:absolute;top:3638px;width:228px;height:242px}

/* footer */
.footer{position:absolute;left:0;top:3885px;width:1200px;height:368px;background:var(--footer);color:var(--white)}
.footer h4{position:absolute;font-size:16px;font-weight:600}
.links{position:absolute;left:162px;top:130px;list-style:none;font-size:12.5px}
.links li{height:29px;display:flex;gap:12px;color:#e8e8e8}
.links li::before{content:"›";color:#aaa}
.vrule{position:absolute;top:88px;width:1px;height:200px;background:#5a5a5a}
.cinfo{position:absolute;left:441px;display:flex;gap:14px;font-size:13px;line-height:20px}
.cicon{width:36px;height:36px;border-radius:50%;border:1.5px solid var(--gold);display:flex;align-items:center;justify-content:center;flex:none}
.cicon svg{width:16px;height:16px}
.social{position:absolute;top:196px;width:30px;height:30px;border-radius:50%;border:1.5px solid #ddd}
.copy{position:absolute;left:0;top:4253px;width:1200px;height:51px;background:var(--teal-dark);color:#e9f1f0;font-size:12px;display:flex;align-items:center;justify-content:center}
</style>
</head>
<body>

<header class="site-header">
  <div class="brand"><span class="brand-dot"></span>Quiet Harbor Path</div>
  <nav class="nav">
    <span class="active">Home</span><span>About</span><span>How We Can Help</span><span>Shared Experiences</span><span>Contact</span>
  </nav>
  <div class="btn" style="left:968px;top:36px;width:120px;height:34px;font-size:13px">Book Now</div>
</header>

<section class="hero" role="img" aria-label="Photo of a coach in conversation with a client at a desk">
  <div class="hero-title">HOLISTIC</div>
  <div class="hero-sub">Transformational Coaching</div>
  <div class="btn" style="left:161px;top:325px;width:136px;height:38px">Book Now</div>
  <div class="arrow" style="left:63px;top:227px;background:var(--white)"><svg viewBox="0 0 14 14"><path d="M9 2L4 7l5 5" stroke="#333" stroke-width="2" fill="none"/></svg></div>
  <div class="arrow" style="left:1098px;top:227px;background:var(--teal)"><svg viewBox="0 0 14 14"><path d="M5 2l5 5-5 5" stroke="#fff" stroke-width="2" fill="none"/></svg></div>
</section>

<h2 class="section-title" style="top:678px">What We Can Do For You</h2>

<div class="card" style="left:163px;top:769px"><div class="icon" role="img" aria-label="Healthy mind illustration"></div><h3>Healthy Mind<br>&amp; Body Life Coaching</h3><p>Lorem ipsum dolor sit amet, consecte adipiscing elit.</p></div>
<div class="card" style="left:385px;top:769px"><div class="icon filled" role="img" aria-label="Consultation illustration"></div><h3>1:1 Life Coaching<br>Consultation</h3><p>Lorem ipsum dolor sit amet, consecte adipiscing elit.</p></div>
<div class="card" style="left:607px;top:769px"><div class="icon" role="img" aria-label="Career growth illustration"></div><h3>Career Analysis Life<br>Coaching</h3><p>Lorem ipsum dolor sit amet, consecte adipiscing elit.</p></div>
<div class="card" style="left:830px;top:769px"><div class="icon" role="img" aria-label="Behaviour coaching illustration"></div><h3>Mind Your Behaviour Life<br>Coaching</h3><p>Lorem ipsum dolor sit amet, consecte adipiscing elit.</p></div>

<div class="card" style="left:163px;top:1041px"><div class="icon" role="img" aria-label="Online coaching illustration"></div><h3>Online<br>Life Coaching</h3><p>Lorem ipsum dolor sit amet, consecte adipiscing elit.</p></div>
<div class="card" style="left:385px;top:1041px"><div class="icon" role="img" aria-label="Hypnosis illustration"></div><h3>Hypnosis for Anxiety,<br>Addictions &amp; Habits</h3><p>Lorem ipsum dolor sit amet, consecte adipiscing elit.</p></div>
<div class="card" style="left:607px;top:1041px"><div class="icon" role="img" aria-label="Keynote speaker illustration"></div><h3>Inspirational Keynote<br>Speaker</h3><p>Lorem ipsum dolor sit amet, consecte adipiscing elit.</p></div>
<div class="card" style="left:830px;top:1041px"><div class="icon" role="img" aria-label="Leadership illustration"></div><h3>Executive Coaching &amp;<br>Leadership Development</h3><p>Lorem ipsum dolor sit amet, consecte adipiscing elit.</p></div>

<section class="about">
  <div class="about-photo" role="img" aria-label="Portrait of a smiling coach holding a clipboard"></div>
  <h2>About Us</h2>
  <div class="kicker">Hi, I'm Quiet Harbor Path</div>
  <p class="lead">Phasellus eu quam a dolor elementum aliquet morbimal sollicitudin vitae eros in fermentum.</p>
  <p class="body">Lorem ipsum dolor sit amet, consectetur adipiscing elit. Seddonec imperdiet dui nec sem iaculis mollis. Sed congue nequemen velit, in vehicula ipsum cursus vel. Donec dui mauris, blandit ac bibendeum pellentesque accumsan, pharetra convallis lectus. Nullam vel duiiw pharetra, varius dolor nect, sodales nunc. Nulla ultrices fermentum porta. Praesent dolor diam, sagittis sed quam nec</p>
  <div class="btn" style="left:632px;top:431px;width:111px;height:36px;font-size:13px">Read More</div>
</section>

<h2 class="section-title" style="top:2018px">Shared Experiences</h2>
<div class="quote-card" style="left:197px;top:2119px;width:170px;height:187px;opacity:.55">
  <p style="font-size:11px;line-height:21px;padding:14px 8px 0">Kind words shared after a calm and steady session together.</p>
  <div class="who" style="font-size:12px;margin-top:28px">GENIE DOE</div>
</div>
<div class="quote-card" style="left:833px;top:2119px;width:170px;height:187px;opacity:.55">
  <p style="font-size:11px;line-height:21px;padding:14px 8px 0">Kind words shared after a calm and steady session together.</p>
  <div class="who" style="font-size:12px;margin-top:28px">GENIE DOE</div>
</div>
<div class="quote-card" style="left:364px;top:2100px;width:472px;height:228px">
  <p style="font-size:14px;line-height:24px;padding:34px 30px 0">"Duis autem vel eum iriure dolor in hendrerit in vulputate velit esse molestie consequat, vel illum dolore eu feugiat nullam facilisis at vero eros et accumsan iusto odiomn dignissi qui blandit praesent luptatum zzril delenit augue duis dolore te feugait nulla facilisi."</p>
  <div class="who" style="font-size:15px;margin-top:12px">GENIE DOE</div>
  <div style="font-size:12px;margin-top:4px">Lorem Ipsum</div>
</div>
<div class="abs" style="left:580px;top:2080px;font-size:46px;font-weight:700;color:var(--gold);line-height:1">”</div>
<div class="arrow" style="left:102px;top:2198px;background:var(--white);box-shadow:0 1px 5px rgba(0,0,0,.15)"><svg viewBox="0 0 14 14"><path d="M9 2L4 7l5 5" stroke="#333" stroke-width="2" fill="none"/></svg></div>
<div class="arrow" style="left:1062px;top:2198px;background:var(--white);box-shadow:0 1px 5px rgba(0,0,0,.15)"><svg viewBox="0 0 14 14"><path d="M5 2l5 5-5 5" stroke="#333" stroke-width="2" fill="none"/></svg></div>
<div class="dots"><span class="on"></span><span></span><span></span><span></span></div>

<h2 class="start-title">Not Sure Where<br>to Start?</h2>
<p class="start-text">Book A Free 15–30 Minute Phone Life Coaching Mini Session with Quiet Harbor Path.</p>
<div class="btn" style="left:161px;top:2742px;width:128px;height:37px;font-size:13px">Book Now</div>
<div class="start-photo" role="img" aria-label="Photo of a speaker presenting to a seated group"></div>

<section class="contact">
  <h2>Get In Touch</h2>
  <p class="intro">Lorem ipsum dolor sit amet consectetur adipiscing elit Sed imperdiet dui nec sem iaculis.</p>
  <div class="field" style="left:67px;top:167px;width:293px;height:35px">Name</div>
  <div class="field" style="left:375px;top:167px;width:293px;height:35px">Email</div>
  <div class="field" style="left:67px;top:219px;width:293px;height:35px">Phone</div>
  <div class="field" style="left:375px;top:219px;width:293px;height:35px">Company</div>
  <div class="field" style="left:67px;top:270px;width:601px;height:89px">Message</div>
  <div class="btn" style="left:311px;top:399px;width:112px;height:35px;font-size:13px">Submit</div>
  <div class="fold"></div><div class="fold-cut" style="border-right-width:0"></div>
</section>

<h2 class="insta-title">INSTAGRAM</h2>
<div class="insta-handle">@QuietHarborPath</div>
<div class="tile" style="left:0;background:linear-gradient(135deg,#2a2a2a,#8a7a6e)" role="img" aria-label="Photo of a man in a beanie holding a phone"></div>
<div class="tile" style="left:233px;background:linear-gradient(180deg,#4a7bb8,#c9d6e0 55%,#6a4b3a)" role="img" aria-label="Photo of hikers in red jackets on a mountain"></div>
<div class="tile" style="left:479px;background:linear-gradient(180deg,#6a8fb0,#3a3a3a 60%,#b0816a)" role="img" aria-label="Photo of a traveller above a mountain village"></div>
<div class="tile" style="left:725px;background:linear-gradient(180deg,#5a4d4a,#e08a3a 50%,#2a1d18)" role="img" aria-label="Photo of a person with raised arms at sunset"></div>
<div class="tile" style="left:971px;width:229px;background:linear-gradient(180deg,#1e2a4a,#5a6a9a 55%,#1a1a28)" role="img" aria-label="Photo of a person on a ridge under a starry sky"></div>

<footer class="footer">
  <h4 style="left:162px;top:88px">Quick Links</h4>
  <ul class="links"><li>Home</li><li>About</li><li>How We Can Help</li><li>Shared Experiences</li><li>Contact</li><li>Book Now</li></ul>
  <div class="vrule" style="left:384px"></div>
  <h4 style="left:440px;top:88px">Contact Details</h4>
  <div class="cinfo" style="top:131px"><div class="cicon"><svg viewBox="0 0 16 16"><path d="M8 1a5 5 0 0 0-5 5c0 4 5 9 5 9s5-5 5-9a5 5 0 0 0-5-5z" fill="none" stroke="#c9a550" stroke-width="1.4"/><circle cx="8" cy="6" r="1.8" fill="#c9a550"/></svg></div><div>PO Box 123<br>Area Name, Country 12345</div></div>
  <div class="cinfo" style="top:188px"><div class="cicon"><svg viewBox="0 0 16 16"><path d="M3 2l3 0 1 3-2 1a8 8 0 0 0 5 5l1-2 3 1 0 3c-7 0-11-4-11-11z" fill="none" stroke="#c9a550" stroke-width="1.4"/></svg></div><div>Phone<br>+1 012-345-6789</div></div>
  <div class="cinfo" style="top:245px"><div class="cicon"><svg viewBox="0 0 16 16"><path d="M1 8l14-6-5 13-2-5z" fill="none" stroke="#c9a550" stroke-width="1.4"/></svg></div><div>Email<br>inquiry@quietharborpath.com</div></div>
  <div class="vrule" style="left:730px"></div>
  <div class="abs" style="left:785px;top:122px;font-size:26px;font-weight:300;display:flex;align-items:center;gap:10px"><span style="width:24px;height:24px;border-radius:50%;background:var(--gold)"></span>Quiet Harbor Path</div>
  <div class="social" style="left:831px" aria-label="Social profile"></div>
  <div class="social" style="left:868px" aria-label="Social profile"></div>
  <div class="social" style="left:905px" aria-label="Social profile"></div>
  <div class="social" style="left:942px" aria-label="Social profile"></div>
</footer>
<div class="copy">Copyright © 2021 Quiet Harbor Path. All Rights Reserved.</div>

</body>
</html>
```